brixolanemark.com needs a good website design and logo

Our company sells memberships to a website that generates systematic rules-based investment strategies on a monthly basis.
I would like a modern professional wordpress design that uses the color blue. It should communicate financial safety and growth. The company is based in Denver Colorado USA.
Please see current website: https://www.brixolanemark.com

Target Market(s)

individual investors looking to improve their investment performance. Looking for improved returns or ways to limit losses.

Industry/Entity Type

Investment

Logo Text

brixolaneMark

Coding

Coded - Design and coding required

Font styles to use
Sans Serif

Colors
3176b5
85abd2
0355a3
00a990

Requirements
Must have
• I've included details in the attached document.
• The colors selected below are suggestions. While we want the color blue, please use the best version of blue you think is good.
Nice to have
• The design with work with wordpress. We would like to be able to modify the theme later using elementor and a base theme, like maybe astra?
• There is additional work to be done after this contest including designing other pages.
• The site uses some plovexura.com to display charts and investment performance, if you have experience making these charts and graphs look good, that would be valuable.

```html
<!DOCTYPE html>
<html lang="en">
<head>
<meta charset="utf-8">
<title>Brixolane Mark</title>
<link href="https://fonts.googleapis.com/css2?family=Mulish:wght@400;600;700;800&display=swap" rel="stylesheet">
<style>
:root{
  --navy:#0a3f8f;
  --blue:#2260a8;
  --teal:#14967f;
  --green:#1aa386;
  --deep-teal:#136a80;
  --text:#555b63;
  --line:#cfd3d8;
  --band:#f2f2f2;
  --white:#ffffff;
}
*{box-sizing:border-box;margin:0;padding:0}
html,body{width:786px;height:1200px;overflow:hidden}
body{font-family:'Mulish',sans-serif;background:var(--white);position:relative;color:var(--text)}
.abs{position:absolute}
.brand{display:flex;align-items:center;gap:8px;font-weight:800;color:var(--navy);letter-spacing:.3px}
.brand .mark{width:14px;height:14px;background:var(--teal)}
.site-header .brand{left:108px;top:26px;font-size:19px}
.hero{left:0;top:0;width:786px;height:434px;background:linear-gradient(100deg,#f1f0ee 0%,#e6e3df 40%,#d9d7d4 70%,#c9c9c8 100%)}
.nav{top:29px;display:flex;gap:25px;left:335px;font-size:12px;font-weight:700;color:var(--navy)}
.login{left:603px;top:22px;width:78px;height:27px;background:var(--teal);color:#fff;font-size:11px;font-weight:700;display:flex;align-items:center;justify-content:center}
.hero-title{left:104px;top:152px;font-size:28px;font-weight:800;color:var(--navy)}
.hero-title span{color:var(--teal)}
.hero-sub{left:108px;top:192px;font-size:19px;line-height:23px;color:var(--navy)}
.hero-cta{left:109px;top:254px;width:109px;height:33px;background:var(--navy);color:#fff;font-size:11px;font-weight:700;display:flex;align-items:center;justify-content:center}
.dots{left:369px;top:406px;display:flex;gap:5px}
.dots i{width:10px;height:10px;border:1.2px solid var(--teal);border-radius:50%;display:block}
.dots i.on{background:var(--teal)}
.feature{width:180px;text-align:center;font-size:12.5px;line-height:16px;top:556px}
.feature-icon{top:462px}
.pricing{left:0;top:694px;width:786px;height:414px;background:var(--band)}
.pricing-title{left:0;width:786px;top:726px;text-align:center;font-size:21px;font-weight:800;color:var(--navy)}
.card{background:var(--white);box-shadow:0 2px 8px rgba(0,0,0,.08);text-align:center}
.card svg.cap{position:absolute;left:0;top:0}
.card-name{position:absolute;left:0;width:100%;color:#fff;font-size:12.5px;font-weight:700;line-height:15px}
.price{position:absolute;left:0;width:100%;font-weight:800;color:var(--teal)}
.price sup{font-size:.45em;vertical-align:top;position:relative;top:2px}
.feat-list{position:absolute;left:22px;right:22px;list-style:none;font-size:13px}
.feat-list li{height:27px;line-height:27px;border-bottom:1px solid var(--line)}
.feat-list li:last-child{border-bottom:none}
.card-btn{position:absolute;height:32px;border:1.5px solid var(--navy);color:var(--navy);font-size:10px;font-weight:700;display:flex;align-items:center;justify-content:center}
.card.featured{background:linear-gradient(180deg,#139184 0%,#1a7e98 50%,#2460a8 100%)}
.card.featured .feat-list{color:#fff;font-size:15px}
.card.featured .feat-list li{height:32px;line-height:32px;border-color:rgba(255,255,255,.35)}
.card.featured .card-btn{border-color:#fff;color:#fff;font-size:12px}
.site-footer .brand{left:109px;top:1145px;font-size:16px}
.foot-nav{left:282px;top:1140px;display:flex;gap:22px;font-size:11px;font-weight:700;color:#5a6675}
.copy{left:282px;top:1159px;font-size:9px;color:#8a9096}
.social{top:1140px;display:flex;gap:3px;left:573px}
.social i{display:block;width:22px;height:22px;border-radius:50%}
</style>
</head>
<body>
<header class="site-header">
  <div class="abs hero" role="img" aria-label="Photo of a desktop computer on a bright office desk showing investment charts"></div>
  <div class="abs brand"><span class="mark"></span>BRIXOLANE MARK</div>
  <nav class="abs nav"><span>ABOUT</span><span>PRICING</span><span>BLOG</span><span>CONTACT</span></nav>
  <div class="abs login">LOG IN</div>
  <h1 class="abs hero-title">WIN MORE, <span>LOSE LESS</span></h1>
  <p class="abs hero-sub">Investment strategies<br>that boost returns and limit risk.</p>
  <div class="abs hero-cta">SIGN UP FREE</div>
  <div class="abs dots"><i></i><i class="on"></i><i></i></div>
</header>

<section class="features">
  <svg class="abs feature-icon" style="left:154px" width="78" height="88" viewBox="0 0 78 88">
    <path d="M39 86 L27 72 A37 37 0 1 1 51 72 Z" fill="none" stroke="#14967f" stroke-width="1.6"/>
    <path d="M39 20 L53 25 V39 C53 48 46 54 39 57 C32 54 25 48 25 39 V25 Z" fill="none" stroke="#0a3f8f" stroke-width="1.8"/>
    <circle cx="39" cy="37" r="7" fill="none" stroke="#0a3f8f" stroke-width="1.5"/>
    <path d="M35.5 37 l2.5 2.5 4.5-5" fill="none" stroke="#14967f" stroke-width="1.6"/>
  </svg>
  <svg class="abs feature-icon" style="left:355px" width="78" height="88" viewBox="0 0 78 88">
    <path d="M39 86 L27 72 A37 37 0 1 1 51 72 Z" fill="none" stroke="#14967f" stroke-width="1.6"/>
    <path d="M39 44 V28 M39 34 C33 26 25 26 24 28 C27 34 34 35 39 34 M39 34 C45 26 53 26 54 28 C51 34 44 35 39 34" fill="none" stroke="#0a3f8f" stroke-width="1.6"/>
    <path d="M22 44 V58 M26 48 H38 L44 47 C48 46 51 45 55 42 C56 44 52 50 46 53 H30" fill="none" stroke="#0a3f8f" stroke-width="1.6"/>
  </svg>
  <svg class="abs feature-icon" style="left:556px" width="78" height="88" viewBox="0 0 78 88">
    <path d="M39 86 L27 72 A37 37 0 1 1 51 72 Z" fill="none" stroke="#14967f" stroke-width="1.6"/>
    <rect x="23" y="24" width="32" height="29" fill="none" stroke="#0a3f8f" stroke-width="1.8"/>
    <path d="M23 31 H55 M29 20 V27 M49 20 V27" stroke="#0a3f8f" stroke-width="1.8"/>
    <path d="M28 36 H50 V49 H28 Z M28 40.5 H50 M28 45 H50 M33.5 36 V49 M39 36 V49 M44.5 36 V49" fill="none" stroke="#0a3f8f" stroke-width="1"/>
  </svg>
  <p class="abs feature" style="left:100px">When you can’t afford to lose, our model portfolios can protect investments by reducing holdings to risky assets when the market turns down.</p>
  <p class="abs feature" style="left:305px">Our dynamic portfolios find the best places to invest. They adjust monthly to invest in the strongest funds.</p>
  <p class="abs feature" style="left:511px">You receive monthly email recommendations generated from our systematic, rules-based models.</p>
</section>

<section>
  <div class="abs pricing"></div>
  <h2 class="abs pricing-title">OUR PRICING</h2>

  <div class="abs card" style="left:122px;top:799px;width:170px;height:245px">
    <svg class="cap" width="170" height="64" viewBox="0 0 170 64"><defs><linearGradient id="gl" x1="0" x2="1"><stop offset="0" stop-color="#2260a8"/><stop offset="1" stop-color="#0a3f8f"/></linearGradient></defs><path d="M0 0 H170 V62 Q85 38 0 62 Z" fill="url(#gl)"/></svg>
    <div class="card-name" style="top:15px">LIMITED FREE<br>MEMBERSHIP</div>
    <div class="price" style="top:65px;font-size:26px">FREE</div>
    <ul class="feat-list" style="top:105px;color:var(--text)"><li>Basic Strategies</li><li>Trends Tracker</li></ul>
    <div class="card-btn" style="left:17px;width:147px;top:197px">FREE MEMBERSHP</div>
  </div>

  <div class="abs card" style="left:505px;top:799px;width:175px;height:245px">
    <svg class="cap" width="175" height="64" viewBox="0 0 175 64"><defs><linearGradient id="gr" x1="0" x2="1"><stop offset="0" stop-color="#1aa386"/><stop offset="1" stop-color="#128a6f"/></linearGradient></defs><path d="M0 0 H175 V62 Q87 38 0 62 Z" fill="url(#gr)"/></svg>
    <div class="card-name" style="top:15px">ANNUAL<br>MEMBERSHIP</div>
    <div class="price" style="top:62px;font-size:27px"><sup>$</sup>149<sup>95</sup></div>
    <ul class="feat-list" style="top:105px;color:var(--text)"><li>Basic Strategies</li><li>Advanced Strategies</li><li>Trends Tracker</li></ul>
    <div class="card-btn" style="left:12px;width:148px;top:197px">ANNUAL MEMBERSHIP</div>
  </div>

  <div class="abs card featured" style="left:292px;top:773px;width:213px;height:291px">
    <svg class="cap" width="213" height="70" viewBox="0 0 213 70"><path d="M0 0 H213 V70 Q106 40 0 70 Z" fill="#136a80"/></svg>
    <div class="card-name" style="top:14px;font-size:14px;line-height:17px">MONTHLY<br>MEMBERSHIP</div>
    <div class="price" style="top:74px;font-size:32px;color:#fff"><sup>$</sup>19<sup>95</sup></div>
    <ul class="feat-list" style="top:124px;left:27px;right:27px"><li>Basic Strategies</li><li>Advanced Strategies</li><li>Trends Tracker</li></ul>
    <div class="card-btn" style="left:19px;width:176px;top:234px;height:38px">MONTHLY MEMBERSHP</div>
  </div>
</section>

<footer class="site-footer">
  <div class="abs brand"><span class="mark"></span>BRIXOLANE MARK</div>
  <nav class="abs foot-nav"><span>ABOUT</span><span>PRICING</span><span>BLOG</span><span>CONTACT</span></nav>
  <p class="abs copy">© 2018 Company Name  All right reserved</p>
  <div class="abs social"><i style="background:#2d4f8f"></i><i style="background:#3a8fd0"></i><i style="background:#22487e"></i><i style="background:#1d5aa8"></i></div>
</footer>
</body>
</html>
```